IT Services Company Needs Corporate PPT Template

This is urgent (need a fast turn around). We need a corporate PPT template deck (NOTE: Deck should be in 4:3 ratio) for our IT Services firm that is clean but slick and modern. We tend to lean more towards the flat design look. I'm attaching a zip file which includes our Corporate Branding Guide (which is in progress), color scheme, A PPT deck as inspiration (our logo is on the last slide), our font (LATO). Our newly launched website is located at: http://www.varnexio.com.

As an example of a deck we like see: http://slidemarket.example/item/tidy-allround-office-slides-kit/5918302?WT.ac=category_thumb&WT.seg_1=category_thumb&WT.z_author=PanelMaker
Although we don't want "this" deck - it gives an idea of style.

I'm also attaching a copy of our corporate deck as it is now to give you an idea of the type of content that would appear on various slides. We definitely want the following slides (at least) within the template:

Title Slide
Blank Slide
2 Column - with bullets
2 Column - no bullets
Single Column - no bullets
Single Column - with bullets
Various Charts and Tables (see example deck)
Meet the Team
Offering Slide
Customer Showcase
Timeline
Case Study
Contact US

Note: Being awarded this job will lead to a second job of creating our corporate deck.

Target Market(s)

CIO, CEO, Technology Officers, Sales People, Marketing, IT heads and staff, Customers, Prospective customers

Industry/Entity Type

Business

Requirements
Must have
• See description and attached files

```html
<!DOCTYPE html>
<html lang="en">
<head>
<meta charset="utf-8">
<title>Varnexio Presentation Template</title>
<link rel="stylesheet" href="https://fonts.googleapis.com/css2?family=Lato:wght@300;400;700;900&display=swap">
<style>
:root{
  --blue:#3a9de4;
  --blue-mid:#2f8fd8;
  --navy:#1d4f86;
  --navy-deep:#1b5a94;
  --teal:#3bb4d0;
  --teal-soft:#5dbfd8;
  --teal-light:#8fd3e3;
  --green:#78b800;
  --green-dark:#4a8a12;
  --grey:#6d6e70;
  --ink:#2f3033;
  --muted:#7a7c80;
  --panel:#f0f1f3;
  --ice:#e6f4f8;
}
*{box-sizing:border-box;margin:0;padding:0}
html,body{width:1067px;height:1200px;overflow:hidden;background:#fff}
body{font-family:'Lato',Arial,sans-serif;color:var(--ink)}
.deck{display:grid;grid-template-columns:533px 533px;grid-template-rows:399px 399px 399px;gap:1px;width:1067px;height:1200px;background:#cfd2d6}
.slide{position:relative;background:#fff;overflow:hidden}
.abs{position:absolute}

/* header */
.slide-header{position:absolute;left:0;top:0;width:533px;height:51px}
.slide-header svg{position:absolute;left:0;top:0}
.slide-title{position:absolute;left:38px;top:0;height:51px;line-height:53px;color:#fff;font-size:15px;font-weight:400;white-space:nowrap}
.slide-title b{font-weight:700}
.title-chevron{position:absolute;left:11px;top:17px;width:18px;height:18px;border:1.5px solid #fff;border-radius:3px}
.title-chevron:after{content:"";position:absolute;left:4px;top:5px;width:5px;height:5px;border-top:1.5px solid #fff;border-right:1.5px solid #fff;transform:rotate(45deg)}
.brand{position:absolute;left:430px;top:0;line-height:51px;color:#fff;font-weight:900;font-size:16px;letter-spacing:.3px}

/* footer */
.slide-footer{position:absolute;left:0;bottom:0;width:533px;height:34px;background:var(--panel)}
.page-no{position:absolute;left:11px;top:9px;width:21px;height:18px;border:1px solid #9a9ca0;border-radius:3px;font-size:9px;font-weight:700;text-align:center;line-height:16px;color:#444}
.connect{position:absolute;left:368px;top:12px;font-size:6.5px;font-weight:700;color:#555;letter-spacing:.2px}
.social{position:absolute;top:10px;width:14px;height:14px;border-radius:2px;background:#5d5f63}

/* slide 11 */
.lead-heading{left:25px;top:72px;font-size:20px;font-weight:300;line-height:25px;color:#222}
.lead-text{left:25px;top:124px;width:480px;font-size:8.5px;line-height:12px;color:#555}
.rule{left:25px;top:162px;width:484px;height:1px;background:#c9cbce}
.fact-band{left:25px;top:175px;width:484px;height:71px;background:var(--teal)}
.fact-band p{position:absolute;left:78px;top:22px;width:390px;color:#fff;font-size:11.5px;line-height:14px}
.fact-band b{font-weight:900}
.icon-disc{left:20px;top:12px;width:46px;height:46px;border-radius:50%;background:#fff}
.split-text{color:#fff;font-size:11.5px;line-height:13px}
.split-text b{font-weight:900}
.icon-block{background:#fff;border-radius:3px}

/* slide 9 */
.list-heading{left:39px;top:76px;font-size:16px;color:#111}
.list-heading b{font-weight:900}
.feature-bar{left:39px;width:455px;color:#fff}
.feature-bar h3{position:absolute;left:62px;top:13px;font-size:14px;font-weight:400;white-space:nowrap}
.feature-bar p{position:absolute;left:62px;top:31px;font-size:9px;opacity:.9;white-space:nowrap}
.feature-bar svg{position:absolute;left:14px;top:14px}

/* slide 8 */
.col-panel{left:18px;top:150px;width:496px;height:182px;background:var(--ice)}
.tab-row{left:18px;top:133px;width:492px;height:17px;display:flex}
.tab{flex:1;background:var(--blue-mid);color:#fff;font-size:8.5px;font-weight:700;line-height:17px;padding-left:8px;clip-path:polygon(0 0,calc(100% - 5px) 0,100% 50%,calc(100% - 5px) 100%,0 100%);margin-right:1px}
.col{top:160px;width:116px}
.col h4{font-size:14px;font-weight:400;color:var(--green);line-height:16px}
.col h4 small{display:block;font-size:8.5px;line-height:10px}
.col .sep{height:1px;background:#c9d6da;margin:8px 0 10px}
.col ul{list-style:none;font-size:8.5px;line-height:11px;color:var(--muted)}
.col li{position:relative;padding-left:12px;margin-bottom:2px}
.col li:before{content:"";position:absolute;left:2px;top:4px;width:3px;height:3px;border-radius:50%;background:var(--muted)}

/* slide 6 */
.table-caption{left:18px;top:75px;font-size:9.5px;color:#222}
.table-caption b{font-weight:900}
.data-table{position:absolute;left:18px;top:94px;width:503px;border-collapse:collapse;table-layout:fixed}
.data-table th{height:32px;text-align:left;color:#fff;font-size:9.5px;font-weight:700;padding:6px 8px 0;vertical-align:middle}
.data-table td{height:42px;vertical-align:top;padding:6px 8px 0;border-bottom:1px solid #fff;background:var(--ice)}
.data-table .c1{background-color:var(--teal)}
.data-table .c2{background-color:var(--green);border-left:3px solid var(--green-dark)}
.data-table .c3{background-color:var(--grey);border-left:3px solid #4c4d50}
.data-table .c4{background-color:var(--teal);border-left:3px solid #2b8fa8}
.data-table td.c1{background:var(--ice);color:var(--teal);font-size:11px;line-height:13px}
.data-table td.c2{background:var(--ice);border-left:3px solid #cfe6a8;color:var(--green);font-size:7px;line-height:8.5px}
.data-table td.c3{background:var(--ice);border-left:3px solid #d2d5d8;color:#777;font-size:7px;line-height:8.5px}
.data-table td.c4{background:var(--ice);border-left:3px solid #fff;border-right:5px solid #d6ecf2;color:var(--teal);font-size:21px;font-weight:300;padding-top:7px}
.data-table td.c4 small{font-size:17px}

/* slide 7 */
.pyr-heading{left:38px;top:83px;font-size:17px;color:#111}
.pyr-heading b{font-weight:900}
.pyr-lead{left:38px;top:112px;font-size:10px;font-weight:700;color:var(--green)}
.pyr-list{left:38px;top:132px;width:260px;list-style:none;font-size:10px;line-height:12.5px;color:var(--green)}
.pyr-list li{position:relative;padding-left:14px;margin-bottom:8px}
.pyr-list li:before{content:"";position:absolute;left:2px;top:4px;width:3.5px;height:3.5px;border-radius:50%;background:var(--green)}
.dots{left:38px;width:262px;border-top:1px dotted #9a9ca0}
.pyr-note{left:38px;width:225px;font-size:7.5px;line-height:12px;color:#222}
.pyr-label{left:300px;width:148px;text-align:center;color:#fff}

/* slide 10 */
.contact-band{left:0;height:58px;color:#fff;font-size:19px;font-weight:400}
.contact-band span{position:absolute;left:74px;top:16px;white-space:nowrap}
.contact-band svg{position:absolute;left:28px;top:14px}
</style>
</head>
<body>
<main class="deck">

  <!-- Slide 11 -->
  <section class="slide">
    <header class="slide-header">
      <svg width="533" height="51" viewBox="0 0 533 51"><rect width="533" height="51" fill="#3a9de4"/><polygon points="400,0 413,0 428,51 415,51" fill="#8fcdf2"/><polygon points="396,51 412,14 428,51" fill="#1a1f26"/><polygon points="413,0 533,0 533,51 428,51" fill="#1d4f86"/></svg>
      <span class="title-chevron"></span>
      <h2 class="slide-title">Vivamus vitae <b>LOREM AC</b></h2>
      <span class="brand">Varnexio</span>
    </header>
    <h1 class="abs lead-heading">Many desktop publishing packages<br>and web page editors</h1>
    <p class="abs lead-text">Search for 'lorem ipsum' will uncover many web sites still in their infancy. Various versions have evolved over the years, sometimes by accident, sometimes on purpose (injected humour and the like).</p>
    <div class="abs rule"></div>
    <div class="abs fact-band">
      <div class="abs icon-disc" role="img" aria-label="Globe icon"></div>
      <p><b>IT IS A LONG ESTABLISHED</b> fact that a reader will be distracted by the readable content of a page when looking at its layout.</p>
    </div>
    <svg class="abs" style="left:25px;top:230px" width="484" height="112" viewBox="0 0 484 112">
      <polygon points="95,16 136,16 115,40" fill="#3bb4d0"/>
      <polygon points="346,16 388,16 367,40" fill="#3bb4d0"/>
      <polygon points="252,40 283,10 312,40 484,40 484,111 250,111 287,74" fill="#78b800"/>
      <polygon points="0,40 200,40 226,10 287,74 250,111 0,111" fill="#6d6e70"/>
      <polygon points="268,52 290,74 268,96 246,74" fill="#2e5a1c"/>
    </svg>
    <div class="abs icon-block" style="left:38px;top:284px;width:34px;height:44px;background:none;border:3px solid #fff" role="img" aria-label="Document with light bulb icon"></div>
    <p class="abs split-text" style="left:93px;top:295px">THE POINT OF USING<br><span style="font-weight:400">Ipsum is that it has...</span></p>
    <p class="abs split-text" style="left:304px;top:291px;width:150px"><b>USING CONTENT HERE</b>, content here making it look like.</p>
    <div class="abs icon-block" style="left:452px;top:284px;width:44px;height:44px;opacity:.95" role="img" aria-label="Person silhouette icon"></div>
    <footer class="slide-footer"><span class="page-no">11</span><span class="connect">CONNECT WITH US:</span><span class="social" style="left:438px"></span><span class="social" style="left:461px"></span><span class="social" style="left:484px"></span><span class="social" style="left:506px"></span></footer>
  </section>

  <!-- Slide 9 -->
  <section class="slide">
    <header class="slide-header">
      <svg width="533" height="51" viewBox="0 0 533 51"><rect width="533" height="51" fill="#3a9de4"/><polygon points="400,0 413,0 428,51 415,51" fill="#8fcdf2"/><polygon points="396,51 412,14 428,51" fill="#1a1f26"/><polygon points="413,0 533,0 533,51 428,51" fill="#1d4f86"/></svg>
      <span class="title-chevron"></span>
      <h2 class="slide-title">Vivamus vitae <b>LOREM AC</b></h2>
      <span class="brand">Varnexio</span>
    </header>
    <h1 class="abs list-heading"><b>Maecenas</b> porttitor arcu <b>eget vehicula auctor:</b></h1>
    <div class="abs feature-bar" style="top:112px;height:52px;background:var(--teal-soft)">
      <svg width="32" height="24" viewBox="0 0 32 24"><circle cx="9" cy="6" r="4" fill="#fff"/><rect x="3" y="11" width="12" height="9" rx="4" fill="#fff"/><circle cx="21" cy="15" r="5" fill="none" stroke="#fff" stroke-width="2"/><line x1="25" y1="19" x2="29" y2="23" stroke="#fff" stroke-width="2"/></svg>
      <h3>Curabitur auctor mi sit amet bibendum imperdiet.</h3>
      <p>Aenean aliquet massa vitae est lacinia, vel dignissim mi vehicula.</p>
    </div>
    <div class="abs feature-bar" style="top:171px;height:52px;background:var(--blue)">
      <svg width="32" height="24" viewBox="0 0 32 24"><rect x="2" y="8" width="16" height="13" fill="none" stroke="#fff" stroke-width="2"/><line x1="5" y1="13" x2="12" y2="13" stroke="#fff" stroke-width="2"/><circle cx="22" cy="8" r="6" fill="none" stroke="#fff" stroke-width="2"/><line x1="18" y1="12" x2="14" y2="17" stroke="#fff" stroke-width="2"/></svg>
      <h3>Praesent id orci lacinia, aliquam purus vel, molestie urna.</h3>
      <p>Pellentesque malesuada nunc vel leo fringilla, non dapibus nisl mollis.</p>
    </div>
    <div class="abs feature-bar" style="top:229px;height:55px;background:#1c72b0">
      <svg width="32" height="24" viewBox="0 0 32 24"><rect x="2" y="3" width="26" height="18" fill="none" stroke="#fff" stroke-width="2"/><rect x="8" y="12" width="3" height="6" fill="#fff"/><rect x="13" y="9" width="3" height="9" fill="#fff"/><rect x="18" y="11" width="3" height="7" fill="#fff"/></svg>
      <h3>Cras egestas felis vitae dui volutpat.</h3>
      <p>Duis vitae justo eu sem lobortis vulputate dictum non leo. Vivamus id orci non ?</p>
    </div>
    <div class="abs feature-bar" style="top:289px;height:55px;background:#1f5a96">
      <svg width="32" height="24" viewBox="0 0 32 24"><path d="M2 16 Q16 4 30 16" fill="none" stroke="#fff" stroke-width="2"/><circle cx="8" cy="8" r="3" fill="#fff"/><circle cx="16" cy="6" r="3" fill="#fff"/><circle cx="24" cy="8" r="3" fill="#fff"/><line x1="8" y1="12" x2="8" y2="22" stroke="#fff" stroke-width="2"/><line x1="24" y1="12" x2="24" y2="22" stroke="#fff" stroke-width="2"/></svg>
      <h3>Vivamus sed sapien vitae lectus ultricies consectetur.</h3>
      <p>Vestibulum consequat nisl vel dolor tincidunt, sit amet rutrum justo pulvinar.</p>
    </div>
    <footer class="slide-footer"><span class="page-no">9</span><span class="connect">CONNECT WITH US:</span><span class="social" style="left:438px"></span><span class="social" style="left:461px"></span><span class="social" style="left:484px"></span><span class="social" style="left:506px"></span></footer>
  </section>

  <!-- Slide 8 -->
  <section class="slide">
    <header class="slide-header">
      <svg width="533" height="51" viewBox="0 0 533 51"><rect width="533" height="51" fill="#3a9de4"/><polygon points="400,0 413,0 428,51 415,51" fill="#8fcdf2"/><polygon points="396,51 412,14 428,51" fill="#1a1f26"/><polygon points="413,0 533,0 533,51 428,51" fill="#1d4f86"/></svg>
      <span class="title-chevron"></span>
      <h2 class="slide-title">Nullam ultrices felis non arcu <b>placerat aliquet</b></h2>
      <span class="brand">Varnexio</span>
    </header>
    <svg class="abs" style="left:18px;top:96px" width="36" height="30" viewBox="0 0 36 30"><circle cx="13" cy="12" r="9" fill="#9fd33c" stroke="#5a9a14" stroke-width="3"/><line x1="20" y1="19" x2="30" y2="28" stroke="#5a9a14" stroke-width="4" stroke-linecap="round"/></svg>
    <div class="abs" style="left:144px;top:98px;width:50px;height:20px;border-radius:8px;background:linear-gradient(90deg,#78b800,#3bb4d0)" role="img" aria-label="Handshake icon"></div>
    <svg class="abs" style="left:271px;top:96px" width="54" height="28" viewBox="0 0 54 28"><rect x="2" y="2" width="22" height="22" rx="5" fill="#9fd33c" stroke="#5a9a14" stroke-width="2"/><rect x="22" y="18" width="30" height="6" fill="#3bb4d0"/></svg>
    <svg class="abs" style="left:398px;top:94px" width="28" height="30" viewBox="0 0 28 30"><rect x="1" y="4" width="26" height="25" fill="#fff" stroke="#3bb4d0" stroke-width="2"/><rect x="1" y="4" width="26" height="6" fill="#3bb4d0"/><g fill="#3bb4d0"><rect x="5" y="13" width="4" height="4"/><rect x="12" y="13" width="4" height="4"/><rect x="19" y="13" width="4" height="4"/><rect x="5" y="20" width="4" height="4"/><rect x="12" y="20" width="4" height="4"/><rect x="19" y="20" width="4" height="4"/></g></svg>
    <div class="abs col-panel"></div>
    <div class="abs tab-row"><span class="tab">Vestibulum consequat</span><span class="tab">Nisl vel dolor tincidunt</span><span class="tab">Sit amet rutrum</span><span class="tab">Justo pulvinar</span></div>
    <div class="abs col" style="left:28px">
      <h4>Nam tempor<br>sem vehicula</h4><div class="sep"></div>
      <ul><li>Praesent vehicula dolor sit amet</li><li>Donec faucibus tortor a turpis</li><li>Ut vel leo nec nunc interdum so</li></ul>
    </div>
    <div class="abs col" style="left:151px">
      <h4>5-10 Phasellus</h4><div class="sep"></div>
      <ul><li>Donec faucibus tortor</li><li>Ut vel leo nec nunc in</li><li>Maecenas ac est con</li><li>Integer vehicula pretium cursus.</li></ul>
    </div>
    <div class="abs col" style="left:278px">
      <h4>Sed ultricies<small>(Aenean mollis elit nec porta.)</small></h4><div class="sep"></div>
      <ul><li>Ut vel leo nec nunc</li><li>Maecenas ac est</li><li>Integer vehicula pretium cursus.</li></ul>
    </div>
    <div class="abs col" style="left:406px;width:104px">
      <h4>Vivamus fer-mentum odio ac hendrerit<small>(Aenean mollis elit nec porta.)</small></h4><div class="sep"></div>
      <ul><li>Praesent vehicula dolor sit amet</li></ul>
    </div>
    <footer class="slide-footer"><span class="page-no">8</span><span class="connect">CONNECT WITH US:</span><span class="social" style="left:438px"></span><span class="social" style="left:461px"></span><span class="social" style="left:484px"></span><span class="social" style="left:506px"></span></footer>
  </section>

  <!-- Slide 6 -->
  <section class="slide">
    <header class="slide-header">
      <svg width="533" height="51" viewBox="0 0 533 51"><rect width="533" height="51" fill="#3a9de4"/><polygon points="400,0 413,0 428,51 415,51" fill="#8fcdf2"/><polygon points="396,51 412,14 428,51" fill="#1a1f26"/><polygon points="413,0 533,0 533,51 428,51" fill="#1d4f86"/></svg>
      <span class="title-chevron"></span>
      <h2 class="slide-title">Sample <b>Table</b></h2>
      <span class="brand">Varnexio</span>
    </header>
    <p class="abs table-caption"><b>Maecenas</b> porttitor arcu <b>eget vehicula auctor:</b></p>
    <table class="data-table">
      <colgroup><col style="width:130px"><col style="width:106px"><col style="width:166px"><col style="width:101px"></colgroup>
      <thead><tr><th class="c1">Lorem ipsum dolor</th><th class="c2">Consectetur</th><th class="c3">Adipiscing elit</th><th class="c4">Rhoncus</th></tr></thead>
      <tbody>
        <tr><td class="c1">Nam tempor sem</td><td class="c2">Maecenas porttitor arcu eget vehicula auctor.</td><td class="c3">Maecenas id erat eu sapien dictum rhoncus sed nec lorem.</td><td class="c4">49.5%</td></tr>
        <tr><td class="c1">Phasellus feugiat justo a (US)</td><td class="c2">Quisque non lorem conse-quat, tempor leo eget, tin-cidunt lacus.</td><td class="c3">Pellentesque malesuada nunc vel leo fringilla, non dapibus nisl mollis. Praesent id orci lacinia, aliquam purus vel, molestie urna.</td><td class="c4">2.5%</td></tr>
        <tr><td class="c1">Sed ultricies ligula a nunc</td><td class="c2">Maecenas porttitor arcu eget vehicula auctor.</td><td class="c3">Praesent vehicula dolor sit amet mattis male-suada. Donec faucibus tortor a turpis adipi-scing porta.</td><td class="c4">$163<small>m</small></td></tr>
        <tr><td class="c1">Donec faucibus tortor</td><td class="c2">Aliquam et justo ut sem mattis sodales id vitae ipsum.</td><td class="c3">Integer vehicula mauris at pretium cursus.</td><td class="c4">10.2<small>x</small></td></tr>
        <tr><td class="c1">Phasellus</td><td class="c2">Maecenas porttitor arcu eget vehicula auctor.</td><td class="c3">Maecenas id erat eu sapien dictum rhoncus sed nec lorem.</td><td class="c4">40%</td></tr>
      </tbody>
    </table>
    <footer class="slide-footer"><span class="page-no">6</span><span class="connect">CONNECT WITH US:</span><span class="social" style="left:438px"></span><span class="social" style="left:461px"></span><span class="social" style="left:484px"></span><span class="social" style="left:506px"></span></footer>
  </section>

  <!-- Slide 7 -->
  <section class="slide">
    <header class="slide-header">
      <svg width="533" height="51" viewBox="0 0 533 51"><rect width="533" height="51" fill="#3a9de4"/><polygon points="400,0 413,0 428,51 415,51" fill="#8fcdf2"/><polygon points="396,51 412,14 428,51" fill="#1a1f26"/><polygon points="413,0 533,0 533,51 428,51" fill="#1d4f86"/></svg>
      <span class="title-chevron"></span>
      <h2 class="slide-title">Nullam ultrices felis non arcu <b>placerat aliquet</b></h2>
      <span class="brand">Varnexio</span>
    </header>
    <h1 class="abs pyr-heading"><b>Ut vel</b> leo nec nunc <b>interdum sodales:</b></h1>
    <p class="abs pyr-lead">Nam tempor sem quis nisi imperdiet imperdiet.</p>
    <ul class="abs pyr-list">
      <li>In auctor dui nec ante tincidunt interdum. Sed ultricies ligula a nunc volutpat vehicula.</li>
      <li>Nunc tincidunt lorem non hendrerit tempor. Quisque non lorem tempor tincidunt interdum.</li>
      <li>Ut vel leo nec nunc interdum sodales.</li>
    </ul>
    <div class="abs dots" style="top:230px"></div>
    <p class="abs pyr-note" style="top:244px">Nam tempor sem quis nisi imperdiet imperdiet. In auctor dui nec tincidunt interdum. Sed ultricies ligula a nunc volutpat tincidunt lorem non hendrerit tempor. Quisque non.</p>
    <div class="abs dots" style="top:290px"></div>
    <p class="abs pyr-note" style="top:302px">Lorem Ipsum is simply dummy text of the printing and industry. Lorem Ipsum has been the industry's dummy text ever since the 1500s, when.</p>
    <svg class="abs" style="left:240px;top:108px" width="270" height="240" viewBox="0 0 270 240">
      <polygon points="135,0 202.5,120 67.5,120" fill="#78b800"/>
      <polygon points="67.5,120 202.5,120 205.3,125 64.7,125" fill="#3f7a10"/>
      <polygon points="64.7,125 205.3,125 236.25,180 33.75,180" fill="#3bb4d0"/>
      <polygon points="33.75,180 236.25,180 239.6,186 30.4,186" fill="#2a8fa8"/>
      <polygon points="30.4,186 239.6,186 270,240 0,240" fill="#8fd3e3"/>
    </svg>
    <div class="abs pyr-label" style="top:148px;font-size:12px;font-weight:700;line-height:14px">In<br>commodo<br>ipsum libero</div>
    <div class="abs pyr-label" style="top:192px;font-size:12px;font-weight:300;line-height:14px">$5.2bn<br>27 bids</div>
    <div class="abs pyr-label" style="top:242px;font-size:11.5px;font-weight:700">Lorem ipsum dolor</div>
    <div class="abs pyr-label" style="top:257px;font-size:9px;font-weight:300">consectetur adipiscing elit.</div>
    <div class="abs pyr-label" style="left:280px;width:188px;top:300px;font-size:11.5px;font-weight:700">Praesent vehicula dolor sit</div>
    <div class="abs pyr-label" style="top:315px;font-size:9px;font-weight:300">sit amet mattis malesuada.</div>
    <footer class="slide-footer"><span class="page-no">7</span><span class="connect">CONNECT WITH US:</span><span class="social" style="left:438px"></span><span class="social" style="left:461px"></span><span class="social" style="left:484px"></span><span class="social" style="left:506px"></span></footer>
  </section>

  <!-- Slide 10 -->
  <section class="slide">
    <header class="slide-header">
      <svg width="533" height="51" viewBox="0 0 533 51"><rect width="533" height="51" fill="#3a9de4"/><polygon points="400,0 413,0 428,51 415,51" fill="#8fcdf2"/><polygon points="396,51 412,14 428,51" fill="#1a1f26"/><polygon points="413,0 533,0 533,51 428,51" fill="#1d4f86"/></svg>
      <span class="title-chevron"></span>
      <h2 class="slide-title"><b>CONTACT US</b></h2>
      <span class="brand">Varnexio</span>
    </header>
    <div class="abs" style="left:0;top:51px;width:533px;height:314px;background:linear-gradient(180deg,#b9b4aa 0%,#8f9aa3 45%,#5f6b74 100%)" role="img" aria-label="Photo of a businessman on the phone by an office window overlooking a city"></div>
    <svg class="abs" style="left:0;top:51px" width="533" height="314" viewBox="0 0 533 314" role="img" aria-label="Street map showing the office location">
      <defs><linearGradient id="mapTone" x1="0" y1="0" x2="1" y2="1"><stop offset="0" stop-color="#ece6da"/><stop offset="1" stop-color="#dcd6c9"/></linearGradient></defs>
      <polygon points="370,0 533,0 533,314 218,314" fill="url(#mapTone)"/>
    </svg>
    <div class="abs contact-band" style="top:78px;width:370px;background:rgba(75,180,210,.88);clip-path:polygon(0 0,100% 0,calc(100% - 32px) 100%,0 100%)">
      <svg width="34" height="28" viewBox="0 0 34 28"><rect x="1" y="3" width="32" height="22" rx="2" fill="#fff"/><polyline points="2,4 17,16 32,4" fill="none" stroke="#4bb4d2" stroke-width="2.5"/></svg>
      <span>samplename@varnexio.com</span>
    </div>
    <div class="abs contact-band" style="top:146px;width:334px;background:rgba(120,184,0,.7);clip-path:polygon(0 0,100% 0,calc(100% - 34px) 100%,0 100%)">
      <svg width="34" height="32" viewBox="0 0 34 32"><rect x="8" y="0" width="18" height="32" rx="3" fill="#fff"/><rect x="11" y="4" width="12" height="20" fill="#9dc64a"/><circle cx="17" cy="28" r="1.6" fill="#9dc64a"/></svg>
      <span>+1 555 0142</span>
    </div>
    <div class="abs contact-band" style="top:214px;width:298px;background:rgba(86,160,0,.92);clip-path:polygon(0 0,100% 0,calc(100% - 32px) 100%,0 100%)">
      <svg width="34" height="30" viewBox="0 0 34 30"><path d="M16 6 H4 V26 H24 V16" fill="none" stroke="#fff" stroke-width="3"/><path d="M14 18 L28 4" stroke="#fff" stroke-width="3"/><path d="M19 3 H29 V13" fill="none" stroke="#fff" stroke-width="3"/></svg>
      <span>www.varnexio.com</span>
    </div>
    <footer class="slide-footer"><span class="page-no">10</span><span class="connect">CONNECT WITH US:</span><span class="social" style="left:438px"></span><span class="social" style="left:461px"></span><span class="social" style="left:484px"></span><span class="social" style="left:506px"></span></footer>
  </section>

</main>
</body>
</html>
```